Business Card Update, need to bring life to the card, two sided color

We need a new business card design, are moving and changing addresses and need a new look, we have the logos already attached but need a new style moving forward. Can incorporate the color of the logo (The Green) as well, maybe a solid back? We deal with safety products revolving around static electricity and safety lighting. Would like to keep same font in second logo as well.

Target Market(s)

Electrical Safety, Lighting

Contact Information for Business Card

Lars Whitcombe
Vice President
Office: 555-284-7316
Cell: 555-862-0457
lars@tkwhitcombe.com
www.tkwhitcombe.com
4700 West Cedar Boulevard
Suite #320
Roswell, GA 30412

Font styles to use
Serif
Sans Serif

Requirements
Must have
• Since 1918
Nice to have
• Could use the 100 Year Logo for back of card, would like the back of card to be the same green as logo.
Should not have
• No black cards please.

```html
<!DOCTYPE html>
<html lang="en">
<head>
<meta charset="utf-8">
<title>T.K. Whitcombe Business Card</title>
<link href="https://fonts.googleapis.com/css2?family=Poppins:wght@400;500;600;700&display=swap" rel="stylesheet">
<style>
  :root {
    --brand-green: #0b9a4c;
    --card-white: #f1f1ef;
    --card-edge: #e2e2df;
    --ink: #141414;
    --band-black: #0d0d0d;
    --backdrop: #9a9a9a;
    --on-green: #ffffff;
  }
  html, body {
    margin: 0;
    padding: 0;
    width: 1200px;
    height: 720px;
    overflow: hidden;
    background: var(--backdrop);
    font-family: "Poppins", sans-serif;
  }
  .canvas {
    position: relative;
    width: 1200px;
    height: 720px;
    display: flex;
    align-items: center;
    justify-content: center;
    gap: 40px;
  }
  .card {
    position: relative;
    width: 560px;
    height: 320px;
    overflow: hidden;
    box-sizing: border-box;
  }
  /* Front side */
  .card-front {
    background: var(--card-white);
  }
  .card-front .frame {
    position: absolute;
    inset: 8px;
    border: 6px solid var(--card-edge);
    pointer-events: none;
  }
  .brand {
    position: absolute;
    left: 40px;
    top: 64px;
    width: 260px;
    color: var(--brand-green);
    font-weight: 600;
  }
  .brand-mark {
    width: 58px;
    height: 58px;
    border-radius: 50%;
    background: var(--brand-green);
    margin: 0 0 12px 92px;
  }
  .brand-name {
    font-size: 25px;
    line-height: 1.05;
    margin: 0;
    letter-spacing: -0.2px;
  }
  .brand-sub {
    font-size: 13.5px;
    line-height: 1.25;
    margin: 2px 0 0;
  }
  .brand-since {
    font-size: 10px;
    font-weight: 600;
    letter-spacing: 2.4px;
    text-transform: uppercase;
    margin: 6px 0 0;
  }
  .web-band {
    position: absolute;
    left: 0;
    bottom: 0;
    width: 300px;
    height: 48px;
    background: var(--band-black);
    clip-path: polygon(34px 0, 100% 0, 100% 100%, 0 100%);
    display: flex;
    align-items: center;
    justify-content: center;
    padding-left: 16px;
    box-sizing: border-box;
  }
  .web-band span {
    color: #ffffff;
    font-size: 12.5px;
    font-weight: 500;
    letter-spacing: 3.2px;
    text-transform: uppercase;
  }
  .contact {
    position: absolute;
    left: 320px;
    top: 96px;
    width: 215px;
    color: var(--ink);
  }
  .contact-name {
    margin: 0;
    font-size: 19px;
    font-weight: 700;
    letter-spacing: 0.6px;
    line-height: 1;
    white-space: nowrap;
  }
  .contact-role {
    margin: 5px 0 14px 0;
    font-size: 8px;
    letter-spacing: 2.4px;
    font-weight: 500;
    text-transform: uppercase;
  }
  .contact-address,
  .contact-lines {
    margin: 0;
    font-size: 10.5px;
    font-weight: 600;
    line-height: 1.5;
  }
  .contact-address { margin-bottom: 8px; }
  .contact-lines {
    display: grid;
    grid-template-columns: 48px auto;
  }
  /* Back side */
  .card-back {
    background: var(--brand-green);
    display: flex;
    align-items: center;
    justify-content: center;
    gap: 16px;
  }
  .back-mark {
    width: 62px;
    height: 62px;
    border-radius: 50%;
    background: var(--on-green);
  }
  .back-text { color: var(--on-green); }
  .back-name {
    font-weight: 600;
    font-size: 30px;
    letter-spacing: 1px;
    line-height: 1.1;
    margin: 0;
  }
  .back-since {
    font-weight: 600;
    font-size: 11px;
    letter-spacing: 3px;
    text-transform: uppercase;
    margin: 4px 0 0;
  }
</style>
</head>
<body>
<main class="canvas">
  <section class="card card-front" aria-label="Business card front">
    <div class="frame"></div>
    <div class="brand">
      <div class="brand-mark"></div>
      <p class="brand-name">T.K. Whitcombe</p>
      <p class="brand-sub">Manufacturing Company, Inc.</p>
      <p class="brand-since">Since 1918</p>
    </div>
    <div class="web-band"><span>www.tkwhitcombe.com</span></div>
    <div class="contact">
      <h1 class="contact-name">LARS WHITCOMBE</h1>
      <p class="contact-role">Vice President</p>
      <p class="contact-address">4700 West Cedar Boulevard<br>Suite #320<br>Roswell, GA 30412</p>
      <div class="contact-lines">
        <span>Office:</span><span>555-284-7316</span>
        <span>Cell:</span><span>555-862-0457</span>
        <span>Email:</span><span>lars@tkwhitcombe.com</span>
      </div>
    </div>
  </section>
  <section class="card card-back" aria-label="Business card back">
    <div class="back-mark"></div>
    <div class="back-text">
      <p class="back-name">T.K. WHITCOMBE</p>
      <p class="back-since">Since 1918</p>
    </div>
  </section>
</main>
</body>
</html>
```